Visitenkarte und Briefpapier für Rechtsanwaltskanzlei
Zielgruppe
Neugründung einer Rechtsanwaltskanzlei für Strafrecht mit einem Anwalt
Aufgabenstellung
Ich möchte gerne Briefpapier und Visitenkarten mit einem schlichten aber professionellen Charakter für meine neue Rechtsanwaltskanzlei erstellen lassen. Die Erscheinung soll modern, sachlich und klar sein. Es soll kein Logo verwendet werden, sondern nur der Namensschriftzug "Dr. Harald Obst", gerne in Großbuchstaben. Siehe dazu beispielhaft die Design-Charakter der angegeben Links.
Die Visitenkarte sollen als druckfähiges PDF und das Briefpapier zusätzlich als Word-Dokument geliefert werden.

```html
<!DOCTYPE html>
<html lang="de">
<head>
<meta charset="utf-8">
<title>Visitenkarte – Rechtsanwaltskanzlei Dr. Harald Obst</title>
<link href="https://fonts.googleapis.com/css2?family=Roboto:wght@300;400&display=swap" rel="stylesheet">
<style>
  :root {
    --backdrop: #3b3b3b;
    --card-light: #4d4d4d;
    --card-dark: #3e3e3e;
    --ink: #f2f2f2;
    --ink-soft: #e4e4e4;
    --rule: #d8d8d8;
  }
  * { box-sizing: border-box; margin: 0; padding: 0; }
  html, body {
    width: 1200px;
    height: 1000px;
    overflow: hidden;
    background: var(--backdrop);
    font-family: "Roboto", Helvetica, Arial, sans-serif;
  }
  .canvas {
    position: relative;
    width: 1200px;
    height: 1000px;
  }
  .card {
    position: absolute;
    width: 528px;
    height: 304px;
    border-radius: 14px;
    background: linear-gradient(135deg, var(--card-light), var(--card-dark));
  }
  .card--back { left: 183px; top: 168px; }
  .card--front { left: 473px; top: 549px; }

  .contact {
    position: absolute;
    left: 22px;
    top: 171px;
    color: var(--ink-soft);
    font-weight: 300;
    font-size: 11px;
    line-height: 14.3px;
  }
  .contact p { white-space: nowrap; }
  .contact .dash { line-height: 14px; }

  .identity {
    position: absolute;
    right: 27px;
    top: 220px;
    text-align: right;
    color: var(--ink);
  }
  .identity__practice {
    font-weight: 300;
    font-size: 11px;
    letter-spacing: 3.6px;
    margin-right: -3.6px;
    padding-bottom: 4px;
    border-bottom: 1px solid var(--rule);
    width: 250px;
    margin-left: auto;
  }
  .identity__name {
    font-weight: 300;
    font-size: 25px;
    line-height: 30px;
    letter-spacing: -0.3px;
  }
</style>
</head>
<body>
  <main class="canvas">
    <section class="card card--back" aria-label="Visitenkarte Rückseite">
      <div class="contact">
        <p>Dr. Harald Obst</p>
        <p class="dash">—</p>
        <p>e: info@harald-obst.de</p>
        <p>t: +49 30 5581 2207</p>
        <p class="dash">—</p>
        <p>10117 Berlin/Lindenweg 14</p>
        <p>www.harald-obst.de</p>
      </div>
    </section>

    <section class="card card--front" aria-label="Visitenkarte Vorderseite">
      <div class="identity">
        <p class="identity__practice">RECHTSANWALTSKANZLEI</p>
        <p class="identity__name">Dr. HARALD OBST</p>
      </div>
    </section>
  </main>
</body>
</html>
```